Flyer-Design für persönlichen Lauftrainer
Zielgruppe
Die trabwerk GmbH entwickelt und vertreibt den persönlichen Lauftrainer TOBAN. TOBAN ist ein elektrisch angetriebenes, automatisch gesteuertes Fahrzeug, mithilfe dessen eine Person ein professionell geplantes Lauftraining im Freien absolvieren kann. Das Gerät übernimmt die Trainingssteuerung und fungiert dabei quasi als ein persönlicher Lauftrainer.
Wir sprechen zwei Kundengruppen an:
1. Privatkunden
2. Institutionelle Kunden wie Physiotherapiezentren und -praxen, Sport- und Wellnesshotels, betriebliches Gesundheitsmanagement und Verleihgeschäfte.
Die Gestaltung, Funktionalität und Ausstattung des Geräts spricht jedoch grundsätzlich die Gesamtheit der Läufer und Fun- und Aktivsportler an.
Aufgabenstellung
Für unseren Produktflyer der DINA 4 und beidseitig bedruckt sein soll, suchen wir nach einem sportlichen, kräftigen, dynamischen Design. Das Design sollte für uns im Nachhinein leicht veränderbar sein (Texte, Bilder, etc.), da wir den Flyer für verschiedene geographische Regionen anpassen werden. Hierfür würden wir z.B. Indesign nutzen. Die Texte, die wir Ihnen mitliefern sollten möglichst so übernommen werden. Wenn Sie die Möglichkeit sehen, den Inhalt in anderer Form darzustellen, dann ist das in Ordnung.
Der Text für den Flyer ist folgender:
Slogan zum großen Bild: Sie brauchen einen persönlichen Lauftrainer?
Zu den kleinen Bildern: Schalten Sie TOBAN ein, wählen Sie ihr Trainingsprogramm und es kann los gehen!
Call to Action: Besuchen Sie www.trabwerk.com
Adresse:
trabwerk GmbH
www.trabwerk.com
Text für Flyer:
Ihr Problem
⁃ Sie haben einen vollen Arbeitstag und wollen trotzdem endlich Ihre Fitness verbessern?
⁃ Sie möchten dringend an Ihrer Figur und Ihrem Gewicht arbeiten?
⁃ Sie wollen schon lange an Ihrem ersten 10 Kilometerlauf teilnehmen und sich optimal darauf vorbereiten?
⁃ Sie möchten einen Trainer haben, der Ihnen jederzeit zur Verfügung steht?
⁃ Mit Ihrer Pulsuhr und Ihrer Lauf-App machen Sie nur geringe oder gar keine Trainingsfortschritte?
Unsere Lösung TOBAN Ihr persönlicher Lauftrainer
⁃ bietet Ihnen ein optimales Lauftraining im Freien durch eine kontrollierte, direkte Geschwindigkeitsvorgabe,
⁃ alarmiert Sie nicht nur wenn Sie etwas falsch machen (indirektes Feedback), er zeigt Ihnen wie Sie es richtig machen (direktes Feedback),
⁃ führt dabei Trainingsprogramme aus, die auf Ihre individuellen Fitness- und Leistungsziele zugeschnitten sind,
⁃ verhindert, dass Sie sich beim Training überlasten,
⁃ unterstützt Sie als
⁃ Anfänger beim Trainingseinstieg
⁃ Fortgeschrittene beim Aufba..

```html
<!DOCTYPE html>
<html lang="de">
<head>
<meta charset="utf-8">
<title>TOBAN Flyer – Vorder- und Rückseite</title>
<link href="https://fonts.googleapis.com/css2?family=Roboto:wght@400;700;900&family=Roboto+Condensed:wght@400;700&display=swap" rel="stylesheet">
<style>
  :root {
    --green: #5a9a2c;
    --green-light: #7cb342;
    --orange: #e07a10;
    --ink: #1e2430;
    --text: #2b2b2b;
    --paper: #ffffff;
    --backdrop: #f1f1f1;
    --sky-top: #2f5fb8;
    --sky-bottom: #9cc3ea;
  }
  * { box-sizing: border-box; margin: 0; padding: 0; }
  html, body { width: 1200px; height: 813px; overflow: hidden; background: var(--backdrop); }
  body { position: relative; font-family: "Roboto", Arial, sans-serif; color: var(--text); }

  .page {
    position: absolute; width: 410px; height: 580px;
    background: var(--paper); overflow: hidden;
    box-shadow: 0 2px 10px rgba(0,0,0,.18);
  }
  .page--front { left: 160px; top: 100px; }
  .page--back  { left: 601px; top: 168px; }

  .photo { position: absolute; }
  .layer-text { position: absolute; z-index: 2; }

  /* Vorderseite */
  .front-photo {
    left: 0; top: 0; width: 410px; height: 288px;
    background: radial-gradient(circle at 25% 35%, #f7d77a 0, #d9a04a 18%, #8a6a45 45%, #4d4a44 75%, #3a3a3a 100%);
  }
  .front-kicker {
    left: 18px; top: 294px;
    font-weight: 900; font-size: 17px; color: var(--ink); letter-spacing: .2px;
  }
  .front-kicker .accent { color: var(--orange); }
  .brand-title {
    font-family: "Roboto", sans-serif; font-weight: 900; line-height: .9;
    background: linear-gradient(90deg, var(--green), var(--green-light));
    -webkit-background-clip: text; background-clip: text; color: transparent;
  }
  .front-title { left: 14px; top: 314px; font-size: 68px; letter-spacing: -1px; }

  .problem-list {
    left: 18px; top: 382px; width: 215px; list-style: none;
    font-size: 8.5px; line-height: 1.28;
  }
  .problem-list li { position: relative; padding-left: 12px; margin-bottom: 5px; }
  .problem-list li::before {
    content: "✗"; position: absolute; left: 0; top: -1px;
    color: var(--orange); font-weight: 700; font-size: 11px;
  }
  .problem-list b { font-weight: 700; color: var(--ink); }

  .product {
    position: absolute; z-index: 1;
    background: linear-gradient(160deg, #8ccc4a 0%, #5a9a2c 55%, #2a2a2a 100%);
    border-radius: 40% 40% 12px 12px / 60% 60% 12px 12px;
    opacity: .9;
  }
  .front-product { left: 242px; top: 225px; width: 158px; height: 250px; }

  .logo { display: flex; align-items: center; gap: 5px; }
  .logo-dot { width: 14px; height: 14px; border-radius: 50%; background: var(--orange); }
  .logo-name { font-weight: 700; font-size: 18px; color: var(--ink); line-height: 1; }
  .front-logo { left: 0; width: 410px; top: 543px; justify-content: center; }
  .front-url { left: 0; width: 410px; top: 564px; text-align: center; font-size: 9px; color: var(--ink); }

  /* Rückseite */
  .back-photo {
    left: 0; top: 0; width: 410px; height: 194px;
    background: linear-gradient(180deg, var(--sky-top) 0%, var(--sky-bottom) 58%, #6b5a4c 62%, #3b3b3e 80%, #2d2d30 100%);
  }
  .back-slogan {
    left: 16px; top: 20px; color: #fff;
    font-size: 18px; line-height: 1.2; font-weight: 400; text-transform: uppercase;
  }
  .back-slogan b { font-weight: 900; }

  .back-lead { left: 22px; top: 204px; font-weight: 900; font-size: 18px; color: var(--ink); }
  .back-title-row { left: 22px; top: 226px; display: flex; align-items: center; gap: 5px; }
  .back-title { font-size: 32px; }
  .back-subtitle {
    font-family: "Roboto Condensed", sans-serif; font-weight: 700; font-size: 12px; line-height: 1.05;
    color: var(--orange); text-transform: uppercase;
  }

  .solution-list {
    left: 10px; top: 264px; width: 268px; list-style: none;
    font-family: "Roboto Condensed", sans-serif; font-size: 8.2px; line-height: 1.3;
  }
  .solution-list li { position: relative; padding-left: 13px; margin-bottom: 3.5px; }
  .solution-list li::before {
    content: "✔"; position: absolute; left: 0; top: -1px; color: var(--orange); font-size: 10px;
  }
  .solution-list b { font-weight: 700; color: var(--ink); }
  .solution-list .sub { display: block; }

  .back-product { left: 285px; top: 200px; width: 110px; height: 225px; }

  .steps-heading {
    left: 24px; top: 436px;
    font-family: "Roboto Condensed", sans-serif; font-weight: 700; font-size: 11px; color: var(--orange);
  }
  .steps { position: absolute; left: 0; top: 452px; width: 410px; height: 76px; display: flex; gap: 5px; }
  .step-photo { flex: 1; height: 100%; }
  .step-photo--1 { background: linear-gradient(135deg, #c9d2d8, #e8c6d8 45%, #e3c23a 70%, #6b7a55); }
  .step-photo--2 { background: linear-gradient(135deg, #4a6f96, #e2b7cf 45%, #e2c02e 70%, #5a6a45); }
  .step-photo--3 { background: linear-gradient(135deg, #cfd6cf, #b9c0b8 45%, #e6c32e 65%, #7a8a6a); }

  .back-footer { left: 22px; top: 541px; width: 370px; display: flex; align-items: center; }
  .cta { margin-left: 14px; font-family: "Roboto Condensed", sans-serif; font-weight: 700; font-size: 10px; color: var(--orange); }
  .cta-url { margin-left: 6px; font-family: "Roboto Condensed", sans-serif; font-weight: 700; font-size: 13px; color: var(--ink); }
  .imprint { left: 22px; top: 565px; font-family: "Roboto Condensed", sans-serif; font-size: 6.3px; color: var(--text); white-space: nowrap; }
</style>
</head>
<body>

<section class="page page--front">
  <div class="photo front-photo" role="img" aria-label="Foto: Läufer bindet im Gegenlicht die orangefarbenen Schnürsenkel seiner Laufschuhe"></div>
  <div class="product front-product" role="img" aria-label="Produktbild: grüner Lauftrainer TOBAN mit vier Rädern und Display am Lenker"></div>
  <p class="layer-text front-kicker">AUF DIE PLÄTZE <span class="accent">FERTIG</span></p>
  <h1 class="layer-text brand-title front-title">TOBAN</h1>
  <ul class="layer-text problem-list">
    <li>Sie haben einen vollen Arbeitstag und wollen trotzdem <b>endlich Ihre Fitness verbessern?</b></li>
    <li>Sie möchten dringend an Ihrer <b>Figur</b> und Ihrem <b>Gewicht arbeiten?</b></li>
    <li>Sie wollen schon lange an Ihrem <b>ersten 10 Kilometerlauf teilnehmen</b> und sich <b>optimal</b> darauf <b>vorbereiten?</b></li>
    <li>Sie möchten einen <b>Trainer</b> haben, der Ihnen <b>jederzeit zur Verfügung</b> steht?</li>
    <li>Mit Ihrer Pulsuhr und Ihrer Lauf-App machen Sie nur geringe oder gar keine Trainingsfortschritte?</li>
  </ul>
  <div class="layer-text logo front-logo"><span class="logo-dot"></span><span class="logo-name">trabwerk</span></div>
  <p class="layer-text front-url">www.trabwerk.com</p>
</section>

<section class="page page--back">
  <div class="photo back-photo" role="img" aria-label="Foto: erschöpfter Läufer auf einer Landstraße vor blauem Himmel und Bergen"></div>
  <h2 class="layer-text back-slogan">„Sie brauchen<br>einen <b>persönlichen<br>Lauftrainer?“</b></h2>
  <p class="layer-text back-lead">WIR HABEN DIE LÖSUNG:</p>
  <div class="layer-text back-title-row">
    <span class="brand-title back-title">TOBAN</span>
    <span class="back-subtitle">Ihr persönlicher<br>Lauftrainer?</span>
  </div>
  <ul class="layer-text solution-list">
    <li>Bietet Ihnen ein <b>optimales Lauftraining im Freien</b> durch eine <b>kontrollierte, direkte Geschwindigkeitsvorgabe</b></li>
    <li><b>Alarmiert</b> Sie nicht nur wenn Sie etwas falsch machen (indirektes Feedback), er zeigt Ihnen wie Sie es richtig machen (direktes Feedback)</li>
    <li>Führt dabei <b>Trainingsprogramme</b> aus, die auf Ihre <b>individuellen Fitness- und Leistungsziele</b> zugeschnitten sind</li>
    <li><b>Verhindert,</b> dass Sie sich beim Training <b>überlasten</b></li>
    <li><b>Unterstützt Sie als:</b>
      <span class="sub">- <b>Anfänger</b> beim Trainingseinstieg</span>
      <span class="sub">- <b>Fortgeschrittene</b> beim Aufbautraining</span>
      <span class="sub">- <b>„Profi“</b> bei einer optimalen Wettkampfvorbereitung</span>
    </li>
    <li>Ist <b>jederzeit verfügbar.</b> Sie müssen ihn nur einschalten, Ihr Trainingsprogramm auswählen und schon kann es losgehen.</li>
  </ul>
  <div class="product back-product" role="img" aria-label="Produktbild: grüner Lauftrainer TOBAN von der Seite"></div>
  <p class="layer-text steps-heading">AUFSTELLEN – EINSCHALTEN – UND LOS GEHT’S!</p>
  <div class="steps">
    <div class="step-photo step-photo--1" role="img" aria-label="Foto: Frau stellt das gelbe Gerät vor der Haustür auf"></div>
    <div class="step-photo step-photo--2" role="img" aria-label="Foto: Frau klappt den Lenker des Geräts hoch"></div>
    <div class="step-photo step-photo--3" role="img" aria-label="Foto: Läuferin folgt dem Gerät auf einem Weg"></div>
  </div>
  <div class="layer-text back-footer">
    <div class="logo"><span class="logo-dot"></span><span class="logo-name">trabwerk</span></div>
    <span class="cta">CALL TO ACTION. BESUCHEN SIE:</span>
    <span class="cta-url">www.trabwerk.com</span>
  </div>
  <p class="layer-text imprint">trabwerk GmbH | Lindenweg 8 | D-10115 Musterstadt | T +49 000 123 456 - 0 | F +49 000 123 456 - 700 | E info@trabwerk.com</p>
</section>

</body>
</html>
```